A Hair, Beauty and Nails Wholesalers Needs a Business Card Design

We need a business card design for our company which is being passed from parents to daughter, so we wont to re-launch the company with an updated, modern, sophisticated, elegant, chic and fresh look which still incorporates the original colour scheme of Hot Pink, Dark Grey and White. The original logo which is attached can be used on the card but we would like to see some designs with the logo and some without, as we have not yet decided if we want the logo on the card. The name of our company is 'Velmora Supplies' and the name of our website is VelmoraGlowandPolish.example.au. We specialise in supplying a massive range of Hair, Beauty and Nail products to the industry. We are based in QLD, Australia but ship many orders via our website all across Australia.

```html
<!DOCTYPE html>
<html lang="en">
<head>
<meta charset="utf-8">
<title>Velmora Supplies – Business Card</title>
<link rel="stylesheet" href="https://fonts.googleapis.com/css2?family=Lato:ital,wght@0,400;0,700;1,400&family=Special+Elite&display=swap">
<style>
  :root {
    --hot-pink: #e5097f;
    --dark-grey: #1a1a1a;
    --mid-grey: #8f9192;
    --white: #ffffff;
    --backdrop: #e6e6e8;
  }
  html, body {
    margin: 0;
    width: 1200px;
    height: 926px;
    overflow: hidden;
    background: var(--backdrop);
    font-family: "Lato", Arial, sans-serif;
  }
  .sheet {
    position: relative;
    width: 1200px;
    height: 926px;
  }
  .card {
    position: absolute;
    left: 280px;
    width: 640px;
    height: 391px;
    background: var(--white);
    box-shadow: 0 6px 18px rgba(0,0,0,0.18);
    overflow: hidden;
  }
  .card--front { top: 52px; }
  .card--back { top: 483px; }

  .card__art {
    position: absolute;
    inset: 0;
    width: 100%;
    height: 100%;
  }

  .brand-mark {
    position: absolute;
    display: flex;
    align-items: center;
    gap: 10px;
    color: var(--hot-pink);
    font-family: "Lato", Arial, sans-serif;
    font-weight: 700;
  }
  .brand-mark__dot {
    width: 22px;
    height: 22px;
    border-radius: 50%;
    background: var(--hot-pink);
  }
  .card--front .brand-mark {
    top: 70px;
    right: 40px;
    font-size: 30px;
  }

  .company-name {
    position: absolute;
    top: 150px;
    right: 40px;
    margin: 0;
    color: var(--hot-pink);
    font-size: 29px;
    font-weight: 700;
    letter-spacing: 0.2px;
  }

  .contact {
    position: absolute;
    left: 60px;
    top: 132px;
    color: var(--white);
  }
  .contact__name {
    margin: 0;
    font-size: 21px;
    font-weight: 400;
  }
  .contact__name strong { font-weight: 700; }
  .contact__role {
    margin: 2px 0 26px;
    font-size: 13px;
    opacity: 0.9;
  }
  .contact__list {
    list-style: none;
    margin: 0;
    padding: 0;
    font-size: 15px;
    line-height: 23px;
  }
  .contact__list li {
    display: flex;
    align-items: center;
    gap: 9px;
    white-space: nowrap;
  }
  .contact__icon {
    width: 13px;
    height: 13px;
    flex: none;
  }

  .card--back .brand-mark {
    top: 140px;
    left: 0;
    right: 0;
    justify-content: center;
    font-size: 40px;
  }
  .web-rule {
    position: absolute;
    left: 0;
    right: 0;
    top: 262px;
    display: flex;
    align-items: center;
    gap: 12px;
    color: var(--hot-pink);
  }
  .web-rule__line {
    flex: 1;
    height: 1.5px;
    background: var(--hot-pink);
  }
  .web-rule__url {
    font-size: 13px;
    font-weight: 700;
    letter-spacing: 2.5px;
    text-transform: uppercase;
  }
</style>
</head>
<body>
<main class="sheet">

  <section class="card card--front" aria-label="Business card front">
    <svg class="card__art" viewBox="0 0 640 391" aria-hidden="true">
      <path d="M0 0 H140 C265 20 300 205 440 252 C525 280 600 292 640 288 V391 H0 Z" fill="var(--hot-pink)"/>
      <path d="M140 4 C290 28 325 218 462 244 C545 258 602 248 632 228 C605 262 545 272 460 258 C318 232 282 42 140 4 Z" fill="var(--dark-grey)"/>
      <path d="M360 268 C460 310 565 300 640 258 V292 C565 322 460 322 360 268 Z" fill="var(--mid-grey)"/>
      <path d="M340 282 C450 332 560 332 640 300 V312 C560 340 450 338 340 282 Z" fill="var(--white)"/>
    </svg>

    <div class="brand-mark"><span class="brand-mark__dot"></span>Velmora</div>
    <h1 class="company-name">Velmora Supplies</h1>

    <div class="contact">
      <p class="contact__name"><strong>Maren</strong> Holloway</p>
      <p class="contact__role">manager</p>
      <ul class="contact__list">
        <li>
          <svg class="contact__icon" viewBox="0 0 16 16" aria-hidden="true"><path fill="currentColor" d="M3 1h3l1.5 4-2 1.3a9 9 0 0 0 4.2 4.2L11 8.5l4 1.5v3c0 1-1 2-2 2C6.5 15 1 9.5 1 3c0-1 1-2 2-2z"/></svg>
          (07) 5550 0192
        </li>
        <li>
          <svg class="contact__icon" viewBox="0 0 16 16" aria-hidden="true"><rect x="1" y="3" width="14" height="10" rx="1" fill="currentColor"/><path d="M1.5 3.5 8 9l6.5-5.5" stroke="var(--hot-pink)" stroke-width="1.4" fill="none"/></svg>
          admin@velmoraglowandpolish.example.au
        </li>
        <li>
          <svg class="contact__icon" viewBox="0 0 16 16" aria-hidden="true"><path fill="currentColor" d="M8 0a5.5 5.5 0 0 0-5.5 5.5C2.5 10 8 16 8 16s5.5-6 5.5-10.5A5.5 5.5 0 0 0 8 0zm0 7.8a2.3 2.3 0 1 1 0-4.6 2.3 2.3 0 0 1 0 4.6z"/></svg>
          28 Harlow Street, BROOKVALE, QLD, 4000
        </li>
      </ul>
    </div>
  </section>

  <section class="card card--back" aria-label="Business card back">
    <div class="brand-mark"><span class="brand-mark__dot"></span>Velmora</div>
    <div class="web-rule">
      <span class="web-rule__line"></span>
      <span class="web-rule__url">www.VelmoraGlowandPolish.example.au</span>
      <span class="web-rule__line"></span>
    </div>
  </section>

</main>
</body>
</html>
```